Cards for Employees

We are looking for an Anniversary and a Birthday card to send to our employees. 2 designs.
We send these cards to our employees based on number of years they work at the company.
Check out our website for more info.
www.BrookfieldServices.example
Target Market(s)
Our Employees -
Font styles to use
Sans Serif
Colors
Designer to choose colors to be used in the design.
Requirements
Must have
- Anniversary card - appreciation for hard work and dedication
Logo - no changes

```html
<!DOCTYPE html>
<html lang="en">
<head>
<meta charset="UTF-8">
<title>Brookfield Services – Employee Cards</title>
<link href="https://fonts.googleapis.com/css2?family=Montserrat:wght@300;400;800&family=Great+Vibes&display=swap" rel="stylesheet">
<style>
  :root {
    --page: #ffffff;
    --card: #000000;
    --white: #ffffff;
    --gold: #f5c400;
    --brand-red: #e4101f;
    --confetti-red: #e8263c;
    --confetti-orange: #f7a21b;
    --confetti-blue: #1aa3e0;
    --flag-blue: #1e4fa8;
    --balloon-green: #6ad62e;
    --balloon-yellow: #f6c629;
    --balloon-pink: #e9328f;
    --balloon-purple: #b13fc7;
  }
  html, body {
    margin: 0;
    width: 1200px;
    height: 1200px;
    overflow: hidden;
    background: var(--page);
  }
  .canvas {
    position: relative;
    width: 1200px;
    height: 1200px;
  }
  .card {
    position: absolute;
    left: 294px;
    width: 624px;
    height: 482px;
    background: var(--card);
    overflow: hidden;
    box-shadow: 10px 14px 18px rgba(0,0,0,0.35);
    font-family: "Montserrat", sans-serif;
    color: var(--white);
  }
  .card--anniversary { top: 91px; }
  .card--birthday { top: 641px; }

  .line {
    position: absolute;
    left: 0;
    width: 100%;
    text-align: center;
    line-height: 1;
    margin: 0;
    transform: translateY(-50%);
  }
  .headline { top: 146px; font-weight: 800; font-size: 36px; letter-spacing: 0.5px; }
  .subline  { top: 182px; font-weight: 800; font-size: 24px; }
  .subline .accent { color: var(--gold); }
  .keyword  { top: 218px; font-weight: 300; font-size: 41px; letter-spacing: 1px; }

  .greeting {
    position: absolute;
    left: 0;
    width: 100%;
    height: 70px;
  }
  .greeting .happy {
    position: absolute;
    font-weight: 800;
    font-size: 29px;
    line-height: 1;
  }
  .greeting .occasion {
    position: absolute;
    font-family: "Great Vibes", cursive;
    color: var(--gold);
    font-size: 46px;
    line-height: 1;
  }
  .card--anniversary .greeting { top: 266px; }
  .card--anniversary .happy { left: 213px; top: 0; }
  .card--anniversary .occasion { left: 210px; top: 14px; }
  .card--birthday .greeting { top: 262px; }
  .card--birthday .happy { left: 213px; top: 3px; }
  .card--birthday .occasion { left: 238px; top: 13px; }

  .brand {
    position: absolute;
    left: 0;
    width: 100%;
    text-align: center;
    font-weight: 800;
    color: var(--brand-red);
    font-size: 20px;
    line-height: 1.05;
    letter-spacing: 0.5px;
  }
  .card--anniversary .brand { top: 378px; }
  .card--birthday .brand { top: 361px; }

  .dotted-arc {
    position: absolute;
    left: 250px;
    top: 438px;
    width: 140px;
    height: 50px;
  }

  .confetti-burst {
    position: absolute;
    top: 0;
    width: 200px;
    height: 120px;
  }
  .confetti-burst--left {
    left: 0;
    background: radial-gradient(ellipse at 30% 60%, rgba(232,38,60,0.85), rgba(247,162,27,0.55) 40%, rgba(26,163,224,0.25) 65%, transparent 80%);
  }
  .confetti-burst--right {
    right: 0;
    background: radial-gradient(ellipse at 70% 60%, rgba(232,38,60,0.85), rgba(247,162,27,0.55) 40%, rgba(26,163,224,0.25) 65%, transparent 80%);
  }

  .bunting {
    position: absolute;
    left: 0;
    top: 0;
    width: 624px;
    height: 100px;
    background: linear-gradient(172deg, var(--confetti-red) 0%, var(--confetti-orange) 40%, rgba(30,79,168,0.85) 62%, transparent 80%);
  }

  .balloons {
    position: absolute;
    left: 426px;
    top: 240px;
    width: 198px;
    height: 242px;
    border-radius: 50% 50% 30% 30%;
    background:
      radial-gradient(circle at 30% 20%, var(--balloon-green), transparent 35%),
      radial-gradient(circle at 60% 18%, var(--balloon-yellow), transparent 35%),
      radial-gradient(circle at 25% 50%, var(--balloon-pink), transparent 40%),
      radial-gradient(circle at 55% 60%, #1676d6, transparent 40%),
      radial-gradient(circle at 85% 45%, var(--balloon-purple), transparent 40%),
      radial-gradient(circle at 80% 70%, var(--balloon-green), transparent 40%);
  }
</style>
</head>
<body>
<main class="canvas">

  <section class="card card--anniversary" aria-label="Anniversary card">
    <div class="confetti-burst confetti-burst--left" role="img" aria-label="Burst of colourful confetti streamers"></div>
    <div class="confetti-burst confetti-burst--right" role="img" aria-label="Burst of colourful confetti streamers"></div>

    <h1 class="line headline">APPRECIATION FOR</h1>
    <p class="line subline"><span class="accent">HARD WORK</span> AND</p>
    <p class="line keyword">DEDICATION</p>

    <div class="greeting">
      <span class="happy">HAPPY</span>
      <span class="occasion">Anniversary</span>
    </div>

    <div class="brand">BROOKFIELD<br>SERVICES</div>

    <svg class="dotted-arc" viewBox="0 0 140 50" aria-hidden="true">
      <path d="M4 50 Q70 -20 136 50" fill="none" stroke="#fff" stroke-width="3" stroke-linecap="round" stroke-dasharray="0 7"/>
    </svg>
  </section>

  <section class="card card--birthday" aria-label="Birthday card">
    <div class="bunting" role="img" aria-label="Strings of red, gold and blue party bunting flags"></div>
    <div class="balloons" role="img" aria-label="Bunch of colourful party balloons"></div>

    <h1 class="line headline" style="top:139px">APPRECIATION FOR</h1>
    <p class="line subline" style="top:175px"><span class="accent">HARD WORK</span> AND</p>
    <p class="line keyword" style="top:211px">DEDICATION</p>

    <div class="greeting">
      <span class="happy">HAPPY</span>
      <span class="occasion">Birthday</span>
    </div>

    <div class="brand">BROOKFIELD<br>SERVICES</div>

    <svg class="dotted-arc" viewBox="0 0 140 50" aria-hidden="true">
      <path d="M4 50 Q70 -20 136 50" fill="none" stroke="#fff" stroke-width="3" stroke-linecap="round" stroke-dasharray="0 7"/>
    </svg>
  </section>

</main>
</body>
</html>
```